Simple and Clean business card design

We would like the design to be simple clean and to incorporate our colors.

We are open to your design and talent, we have the dots in our logo as we think of it as data points and we connect data points for people.

We are open to see the great creative and clean design you bring to the table

Contact Information for Business Card

please include: name, position, email, phone and website

Font styles to use
Sans Serif

Requirements
Must have
• my colors incorporated, simplicity
Nice to have
• lots of white space, simplicity
Should not have
• complexicity/ complex art

```html
<!DOCTYPE html>
<html lang="en">
<head>
<meta charset="utf-8">
<title>Nectaro – Business Card</title>
<link rel="stylesheet" href="https://fonts.googleapis.com/css2?family=Poppins:wght@400;500;700&display=swap">
<style>
  :root {
    --backdrop: #2b2b2d;
    --paper: #ffffff;
    --ink: #111111;
    --brand-blue: #507ac0;
    --brand-green: #2ea653;
    --brand-yellow: #f6be17;
    --brand-red: #e94235;
    --divider: #333333;
  }
  * { box-sizing: border-box; margin: 0; padding: 0; }
  html, body {
    width: 1200px;
    height: 900px;
    overflow: hidden;
    background: var(--backdrop);
    font-family: "Poppins", Arial, sans-serif;
    color: var(--ink);
  }
  .stage {
    position: relative;
    width: 1200px;
    height: 900px;
  }
  .card {
    position: absolute;
    left: 290px;
    width: 620px;
    height: 354px;
    background: var(--paper);
    border-radius: 22px;
    overflow: hidden;
  }
  .card--back { top: 60px; }
  .card--front { top: 480px; }

  /* back side */
  .back-mark {
    position: absolute;
    left: 120px;
    top: 97px;
    width: 160px;
    height: 160px;
    border-radius: 50%;
    background: var(--brand-blue);
  }
  .back-website {
    position: absolute;
    right: 48px;
    bottom: 40px;
    font-size: 17px;
    font-weight: 500;
    letter-spacing: 0.5px;
  }

  /* front side */
  .brand-name {
    position: absolute;
    left: 44px;
    top: 40px;
    font-size: 50px;
    font-weight: 500;
    letter-spacing: -0.5px;
    line-height: 1;
    color: var(--ink);
  }
  .holder {
    position: absolute;
    right: 44px;
    top: 44px;
    text-align: right;
  }
  .holder__name {
    font-size: 22px;
    font-weight: 700;
    line-height: 1.2;
  }
  .holder__role {
    font-size: 15px;
    font-weight: 400;
    color: var(--brand-green);
    letter-spacing: 0.3px;
  }
  .contacts {
    position: absolute;
    left: 36px;
    right: 36px;
    bottom: 46px;
    display: flex;
    align-items: center;
    justify-content: space-between;
    font-size: 15px;
    font-weight: 400;
  }
  .contact {
    display: flex;
    align-items: center;
    gap: 9px;
  }
  .contact__icon {
    width: 24px;
    height: 24px;
    border-radius: 50%;
    background: var(--brand-blue);
    display: flex;
    align-items: center;
    justify-content: center;
    flex: none;
  }
  .contact__icon svg { width: 14px; height: 14px; }
  .divider {
    width: 1px;
    height: 18px;
    background: var(--divider);
  }
  .color-band {
    position: absolute;
    left: 0;
    right: 0;
    bottom: 0;
    height: 12px;
    display: flex;
  }
  .color-band__blue { flex: 40; background: var(--brand-blue); }
  .color-band__green { flex: 37; background: var(--brand-green); }
  .color-band__yellow { flex: 23; background: var(--brand-yellow); }
</style>
</head>
<body>
<main class="stage">

  <section class="card card--back" aria-label="Card back">
    <div class="back-mark"></div>
    <p class="back-website">www.nectaro.com</p>
  </section>

  <section class="card card--front" aria-label="Card front">
    <h1 class="brand-name">Nectaro</h1>

    <div class="holder">
      <p class="holder__name">Daniel Reed</p>
      <p class="holder__role">Managing Director</p>
    </div>

    <div class="contacts">
      <div class="contact">
        <span class="contact__icon">
          <svg viewBox="0 0 24 24" fill="#fff"><path d="M6.6 10.8c1.4 2.8 3.8 5.1 6.6 6.6l2.2-2.2c.3-.3.7-.4 1-.2 1.1.4 2.3.6 3.6.6.6 0 1 .4 1 1V20c0 .6-.4 1-1 1C10.6 21 3 13.4 3 4c0-.6.4-1 1-1h3.5c.6 0 1 .4 1 1 0 1.3.2 2.5.6 3.6.1.3 0 .7-.2 1L6.6 10.8z"/></svg>
        </span>
        <span>555-014-2739</span>
      </div>
      <span class="divider"></span>
      <div class="contact">
        <span class="contact__icon">
          <svg viewBox="0 0 24 24" fill="none" stroke="#fff" stroke-width="2"><rect x="3" y="6" width="18" height="12" rx="1"/><path d="M3 7l9 6 9-6"/></svg>
        </span>
        <span>hello@nectaro.com</span>
      </div>
      <span class="divider"></span>
      <div class="contact">
        <span class="contact__icon">
          <svg viewBox="0 0 24 24" fill="none" stroke="#fff" stroke-width="1.8"><circle cx="12" cy="12" r="9"/><path d="M3 12h18M12 3c3 3 3 15 0 18M12 3c-3 3-3 15 0 18"/></svg>
        </span>
        <span>www.nectaro.com</span>
      </div>
    </div>

    <div class="color-band">
      <span class="color-band__blue"></span>
      <span class="color-band__green"></span>
      <span class="color-band__yellow"></span>
    </div>
  </section>

</main>
</body>
</html>
```